Fully coded Word press template and New logo for Colocation Provider

We need a wordpress template and new logo for our website. The current website is vornlukhost.net. Vornluk Host is a colocation provider located in San Antonio Texas. We are looking for a complete re-design of the site and logo. Everything is on the table. New colors, logo, look, feel...everything. Go wild! We are looking for a clean modern look.

P.S. The name Vornluk originated from the Glimmer Forge movies (Vornluk is where the work was done).

Target Market(s)

We are targeting toward IT staffs and CFO's

Requirements
Must have
• Must have clean look. Although can have some playfulness too it, It must convey safety and security.

```html
<!DOCTYPE html>
<html lang="en">
<head>
<meta charset="utf-8">
<title>Vornluk Host Services</title>
<link href="https://fonts.googleapis.com/css2?family=Arimo:wght@400;700&family=Noto+Sans:wght@400&family=Dancing+Script&display=swap" rel="stylesheet">
<style>
:root{
  --brand-teal:#19b3a8;
  --heading-teal:#1fa89a;
  --nav-blue:#1670b8;
  --link-blue:#3d7fd6;
  --title-blue:#2a7fd4;
  --spec-blue:#1766b5;
  --ink:#222;
  --ink-soft:#444;
  --muted:#777;
  --panel-line:#e2e2e2;
  --band:#f9f8f8;
  --hero-deep:#0a6fc2;
  --hero-mid:#1c8be0;
  --hero-light:#4fc3f7;
}
*{margin:0;padding:0;box-sizing:border-box}
html,body{width:1024px;height:1200px;overflow:hidden;background:#fff}
body{position:relative;font-family:"Arimo",Arial,sans-serif;color:var(--ink)}
.abs{position:absolute}
.brand{left:37px;top:53px;font-family:"Noto Sans",sans-serif;font-size:16px;color:#444;display:flex;align-items:center;gap:5px}
.brand .dot{width:13px;height:13px;border-radius:50%;background:#cfd3d6}
.brand .first{color:var(--brand-teal)}
.connect{left:740px;top:30px;font-family:"Dancing Script",cursive;font-size:12px;color:#7fb6d8}
.social{left:829px;top:28px;display:flex;gap:5px}
.social span{width:20px;height:20px;border-radius:3px;background:#5aa6d9}
.account{top:70px;font-family:"Noto Sans",sans-serif;font-size:11px;color:#111}
.panel{left:10px;top:96px;width:1004px;height:686px;border:1px solid var(--panel-line);border-radius:10px;box-shadow:0 0 4px rgba(0,0,0,.06)}
.nav{right:46px;top:100px;display:flex;font-family:"Noto Sans",sans-serif;font-size:12px;color:var(--nav-blue)}
.nav a{color:inherit;text-decoration:none;padding:10px 17px;border-left:1px solid #e6e6e6;height:36px}
.nav a:first-child{border-left:none}
.hero{left:12px;top:136px;width:1000px;height:412px;border-radius:8px;overflow:hidden;
  background:
    radial-gradient(ellipse 230px 250px at 24% 42%,rgba(220,245,255,.85) 0%,rgba(120,210,250,.55) 40%,rgba(40,150,230,0) 75%),
    radial-gradient(ellipse 200px 60px at 62% 30%,rgba(170,235,255,.55),rgba(40,150,230,0) 70%),
    radial-gradient(ellipse 160px 260px at 66% 65%,rgba(120,215,255,.45),rgba(40,150,230,0) 70%),
    linear-gradient(90deg,var(--hero-mid) 0%,var(--hero-light) 30%,var(--hero-mid) 60%,var(--hero-deep) 100%)}
.hero p{position:absolute;left:27px;top:346px;font-family:"Noto Sans",sans-serif;font-size:15px;line-height:20px;color:#fff}
.feature-art{height:66px;border-radius:6px;background:linear-gradient(135deg,#eef4fa,#b9cfe3)}
.feature h3{font-weight:400;font-size:13px;line-height:15px;color:var(--heading-teal);text-transform:uppercase}
.feature p{font-size:11px;line-height:13px;margin-top:3px;color:var(--ink)}
.more{display:flex;align-items:flex-start;gap:2px;font-size:12px;color:var(--link-blue);line-height:14px}
.more i{flex:none;width:46px;height:30px;border-radius:4px;background:linear-gradient(135deg,#9aa7b3,#3f5366)}
.why h2{font-weight:400;font-size:24px;color:var(--title-blue)}
.why p{font-size:13.6px;line-height:17px;color:#333;margin-top:18px;width:970px}
.specs{left:12px;top:910px;width:1000px;height:146px;background:var(--band)}
.specs h2{position:absolute;left:28px;top:22px;font-weight:400;font-size:14px;color:var(--spec-blue)}
.specs p{position:absolute;left:29px;top:53px;width:900px;font-size:11px;line-height:14px;color:var(--ink-soft)}
.footer-links{left:63px;top:1082px;font-size:10px;color:var(--muted)}
.copyright{left:63px;top:1107px;font-size:10px;color:var(--muted)}
.count{left:923px;top:1087px;font-size:11px;color:#111}
</style>
</head>
<body>
<header>
  <div class="abs brand"><span class="dot"></span><span><span class="first">vornluk</span> host services llc</span></div>
  <div class="abs connect">connect with us</div>
  <div class="abs social" aria-label="Social links"><span></span><span></span><span></span><span></span><span></span><span></span></div>
  <div class="abs account" style="left:847px">login</div>
  <div class="abs account" style="left:895px">|</div>
  <div class="abs account" style="left:919px">contact us</div>
</header>

<div class="abs panel"></div>
<nav class="abs nav">
  <a>HOME</a><a>SERVICES</a><a>SAFETY &amp; SECURITY</a><a>DATA CENTER SPECIFICATIONS</a><a>ABOUT US</a>
</nav>

<section class="abs hero" role="img" aria-label="Glowing digital globe wrapped in fiber optic light strands on a blue background">
  <p>With a potent combination of upscale technological sophistication and down-home trustworthy service,<br>Vornluk is the reliable, user-friendly data center solution your growing business demands.</p>
</section>

<div class="abs feature-art" style="left:198px;top:578px;width:118px" role="img" aria-label="Devices connected to a cloud"></div>
<div class="abs feature-art" style="left:568px;top:580px;width:112px;height:64px" role="img" aria-label="Computers and phones around a globe"></div>
<div class="abs feature-art" style="left:852px;top:578px;width:118px" role="img" aria-label="Network of devices linked to a server"></div>

<div class="abs feature" style="left:56px;top:650px;width:290px">
  <h3>Safe, Secure, Invisible</h3>
  <p style="margin-left:-1px">Thieves can't steal it if they don't know it's there, which is why the Vornluk Data Center facility is built to be invisible.</p>
</div>
<div class="abs feature" style="left:376px;top:650px;width:300px">
  <h3>Lower Total Cost of Ownership</h3>
  <p style="margin-left:-1px">The appeal of outsourcing is that it strengthens your cash flow while freeing your company's decision makers from the minutiae of IT management.</p>
</div>
<div class="abs feature" style="left:706px;top:650px;width:292px">
  <h3>Disaster Avoidance</h3>
  <p style="margin-left:-1px">If the biggest known threat to data security were sand,<br>would you store your data on the beach? Neither would we.</p>
</div>

<a class="abs more" style="left:37px;top:714px"><i role="img" aria-label="Binoculars"></i><span style="margin-top:13px">Tour The Most Secure Data Facility In Texas</span></a>
<a class="abs more" style="left:368px;top:714px;width:290px"><i role="img" aria-label="Document icon" style="width:32px"></i><span style="margin-top:13px;margin-left:2px">How Data Outsourcing Can Strengthen Your Bottom Line</span></a>
<a class="abs more" style="left:702px;top:714px"><i role="img" aria-label="Globe icon" style="width:32px"></i><span style="margin-top:13px">Tour The Most Secure Data Facility In Texas</span></a>

<section class="abs why" style="left:39px;top:805px">
  <h2>Why Vornluk</h2>
  <p>You need safe, always-on data, and you need unwavering confidence in the partner you choose to manage it. With a potent combination of upscale technological sophistication and down-home trustworthy service, Vornluk is the reliable, user-friendly data center solution your growing business demands.</p>
</section>

<section class="abs specs">
  <h2>Data Center Specifications</h2>
  <p>The deeper you dig into Vornluk's hardware and equipment specifications, the clearer it becomes that the facility is engineered to deliver optimum performance, always-on data access, and lockdown security. Moreover, its design allows and encourages continuous enhancement, ensuring that Vornluk can provide best in calls technology and service levels today, and continue to do so far into the future.</p>
</section>

<footer>
  <div class="abs footer-links">Home | Services | Safety &amp; Security | Data Center Specifications | About Us | Contact Us</div>
  <div class="abs copyright">Copyright 2012 Vornluk Host Services, All Rights Reserved.</div>
  <div class="abs count">x15</div>
</footer>
</body>
</html>
```